Website for Party

Design a new website for PlumtreeGatherings.net
We have attached the new logos and please look at the website, and our facebook page: facebook.com/plumtreegatherings for inspiration
Updates

Hi Guys, please be original with all designs and images otherwise the design will be eliminated Thank you

some of your designs have too much happening in them, others make it clear that the designer has not yet read the brief fully

Please everyone be original!

```html
<!DOCTYPE html>
<html lang="en">
<head>
<meta charset="utf-8">
<title>PlumtreeGatherings.net</title>
<link rel="stylesheet" href="https://fonts.googleapis.com/css2?family=Cinzel:wght@400;700&family=Open+Sans:wght@400;700&family=Raleway:wght@300;400&display=swap">
<style>
  :root {
    --plum-deep: #2a0d22;
    --plum-mid: #5e1f4a;
    --plum-glow: #8a3a6c;
    --text-light: #f2e6ee;
    --text-soft: #c9b3c2;
    --banner-light: #f4f4f6;
    --banner-shade: #dcdde2;
    --ink: #1d1d22;
    --button: #ececec;
  }
  * { margin: 0; padding: 0; box-sizing: border-box; }
  html, body { width: 820px; height: 1200px; overflow: hidden; }
  body {
    position: relative;
    background:
      radial-gradient(ellipse 60% 30% at 50% 8%, var(--plum-glow) 0%, transparent 70%),
      radial-gradient(ellipse 80% 40% at 50% 80%, var(--plum-mid) 0%, transparent 75%),
      linear-gradient(180deg, var(--plum-mid) 0%, var(--plum-deep) 55%, var(--plum-mid) 100%);
    color: var(--text-light);
    font-family: "Raleway", sans-serif;
  }
  .brand {
    position: absolute; left: 0; right: 0; text-align: center;
    font-family: "Raleway", sans-serif; font-weight: 400; color: var(--text-light);
    line-height: 1;
  }
  .brand-top { top: 44px; font-size: 38px; letter-spacing: 2px; }
  .brand-top small { display: block; font-size: 11px; letter-spacing: 3px; margin-top: 8px; }
  .brand-foot { top: 1026px; font-size: 30px; letter-spacing: 2px; }
  .main-nav {
    position: absolute; top: 156px; left: 200px; right: 150px;
    display: flex; justify-content: space-between;
    font-size: 14px; letter-spacing: 1px; text-transform: uppercase; color: var(--text-soft);
  }
  .hero {
    position: absolute; top: 219px; left: 0; width: 820px; height: 306px;
    background: linear-gradient(180deg, var(--banner-light), var(--banner-shade));
  }
  .hero-text { position: absolute; left: 40px; top: 58px; color: var(--ink); font-family: "Open Sans", sans-serif; }
  .hero-text h1 { font-size: 30px; font-weight: 700; line-height: 1.2; }
  .hero-text ul { list-style: none; margin-top: 10px; font-size: 15px; line-height: 1.5; }
  .hero-text li::before { content: "•"; margin-right: 4px; }
  .hero-photo {
    position: absolute; left: 410px; top: 0; width: 410px; height: 306px;
    background: linear-gradient(135deg, #b8b9c4 0%, #6a2b3e 35%, #2c2a3a 60%, #c89a3a 100%);
  }
  .slider-dots { position: absolute; top: 543px; left: 0; right: 0; text-align: center; }
  .slider-dots span { display: inline-block; width: 7px; height: 7px; border-radius: 50%; background: var(--text-light); margin: 0 6px; }
  .features { position: absolute; top: 628px; left: 55px; width: 720px; display: flex; justify-content: space-between; }
  .feature { width: 205px; }
  .feature-photo { height: 124px; }
  .photo-club { background: linear-gradient(160deg, #2a1b4a, #8a3fd0 60%, #c8a0f0); }
  .photo-harbor { background: linear-gradient(180deg, #3b3f8a, #8a6bb0 55%, #1a1c3a); }
  .photo-stage { background: radial-gradient(circle at 40% 50%, #3a3a3a, #050505 70%); }
  .feature h2 {
    font-family: "Cinzel", serif; font-weight: 700; font-size: 12px; text-transform: uppercase;
    margin-top: 18px; line-height: 1.35; color: var(--text-light); height: 33px;
  }
  .feature p { font-family: "Cinzel", serif; font-size: 9.5px; line-height: 1.45; margin-top: 6px; color: var(--text-soft); height: 84px; overflow: hidden; }
  .more-btn {
    display: block; width: 52px; margin: 10px auto 0; background: var(--button); color: var(--ink);
    font-family: "Open Sans", sans-serif; font-weight: 700; font-size: 10px; text-align: center; padding: 3px 0;
  }
  .divider { position: absolute; top: 958px; left: 40px; right: 40px; height: 1px; background: rgba(242,230,238,0.25); }
  .page-arrow { position: absolute; top: 1038px; }
  .page-arrow.prev { left: 40px; }
  .page-arrow.next { right: 40px; }
  .social { position: absolute; top: 1108px; left: 0; right: 0; display: flex; justify-content: center; gap: 6px; }
  .social span { width: 17px; height: 17px; background: var(--text-light); border-radius: 2px; }
</style>
</head>
<body>
  <div class="brand brand-top">Plumtree<small>PlumtreeGatherings.net</small></div>

  <nav class="main-nav">
    <span>Welcome</span><span>About</span><span>Order Tickets</span><span>Contact</span><span>FAQ</span>
  </nav>

  <section class="hero">
    <div class="hero-text">
      <h1>July 4th Yacht Party<br>Music by DJ Marlo</h1>
      <ul>
        <li>Opening Performance by Tovin Reyes</li>
        <li>Luxury Party</li>
        <li>Open Bar</li>
      </ul>
    </div>
    <div class="hero-photo" role="img" aria-label="Collage of party photos with the DJ, fireworks, flags and drinks"></div>
  </section>

  <div class="slider-dots"><span></span><span></span><span></span><span></span></div>

  <section class="features">
    <article class="feature">
      <div class="feature-photo photo-club" role="img" aria-label="Dance floor lit in purple light"></div>
      <h2>Epic Mixes by DJ Marlo</h2>
      <p>Hit the floor and enjoy nonstop DJ Marlo's epic sessions with millions of light combinations on the dance floor. DJ Marlo will entertain with nightlife sessions.</p>
      <span class="more-btn">MORE</span>
    </article>
    <article class="feature">
      <div class="feature-photo photo-harbor" role="img" aria-label="City skyline across the harbor at dusk"></div>
      <h2>3+ Hour Cruise Around NYC Harbor</h2>
      <p>Over 3 hours of cruising through the NYC harbor. Enjoy the open-air deck and admire breathtaking views of Manhattan's stunning skyline at sunset with your sweetheart.</p>
      <span class="more-btn">MORE</span>
    </article>
    <article class="feature">
      <div class="feature-photo photo-stage" role="img" aria-label="Performer on a dark stage"></div>
      <h2>Opening Performance by Tovin Reyes</h2>
      <p>Up and coming musical sensation Tovin Reyes will perform the national anthem to kick off the cruise, and he will lead an acoustic session on the outdoor deck of the yacht.</p>
      <span class="more-btn">MORE</span>
    </article>
  </section>

  <div class="divider"></div>

  <svg class="page-arrow prev" width="14" height="24" viewBox="0 0 14 24"><polygon points="14,0 0,12 14,24" fill="rgba(242,230,238,0.25)"/></svg>
  <svg class="page-arrow next" width="14" height="24" viewBox="0 0 14 24"><polygon points="0,0 14,12 0,24" fill="rgba(242,230,238,0.25)"/></svg>

  <div class="brand brand-foot">Plumtree</div>

  <div class="social"><span></span><span></span><span></span><span></span><span></span><span></span></div>
</body>
</html>
```